limo company looking for a graphic business card with professional look and feel

Looking for a business card design that can give you the full picture of the limo company by looking at the card - we provide airport service, wedding, birthday, night out, etc... we have sedans, suvs , limos, and party buses. I want the business card to have a professional look because we are targetting corporate clients as well as regular retail.
Info about the business can be found at: http://qivroe.example/Tm3Kx7
Target Market(s)
corporate clients and retail
Industry/Entity Type
Business
Contact Information for Business Card
I would like the logo and the name of the company to be in raised print - not sure if design makes a difference for that or just print - I need it designed in 350dpi
Requirements
Must have
- pictures of vehicle types (sedans, suvs, limos, party bus). pictures of interior of the limos if possible. list service types (weddings, birthdays, proms, airport transportation) & service areas (houston, the woodlands, spring, tomball, cypress, kingwood).
Nice to have
- nice professional look to it.

```html
<!DOCTYPE html>
<html lang="en">
<head>
<meta charset="utf-8">
<title>Marlow Limousine – Business Card</title>
<link rel="stylesheet" href="https://fonts.googleapis.com/css2?family=Open+Sans:wght@400;600;700&display=swap">
<style>
  :root {
    --backdrop: #e9e6e1;
    --card: #050505;
    --ink: #ffffff;
    --ink-soft: #d9d9d9;
    --rule: #ffffff;
    --photo-blue-a: #2b3f8f;
    --photo-blue-b: #0b1030;
    --photo-green-a: #3ccf7a;
    --photo-green-b: #0a3d22;
    --silhouette: #1a1a1a;
  }
  * { box-sizing: border-box; margin: 0; padding: 0; }
  html, body {
    width: 1200px; height: 780px; overflow: hidden;
    background: var(--backdrop);
    font-family: "Open Sans", Arial, sans-serif;
    color: var(--ink);
  }
  .sheet {
    position: relative; width: 1200px; height: 780px;
    display: flex; align-items: center; justify-content: center; gap: 50px;
  }
  .card {
    position: relative; width: 540px; height: 308px;
    background: var(--card); overflow: hidden;
    box-shadow: 0 10px 24px rgba(0,0,0,.25);
  }
  .card-art { position: absolute; inset: 0; width: 100%; height: 100%; }

  .brand { position: absolute; line-height: 1.1; font-weight: 600; color: var(--ink); }
  .brand-name { font-size: 24px; letter-spacing: .5px; display: block; }
  .brand-tag { font-size: 13px; display: block; padding-left: 40px; }

  .front .brand { left: 28px; top: 118px; }

  .contact { position: absolute; left: 300px; top: 128px; }
  .contact-name { font-size: 22px; font-weight: 700; line-height: 1.1; }
  .contact-role { font-size: 13px; color: var(--ink-soft); margin-bottom: 8px; }
  .contact-line { display: flex; align-items: center; gap: 8px; font-size: 13px; line-height: 1.6; }
  .contact-icon { width: 14px; height: 14px; background: var(--ink); border-radius: 2px; display: inline-flex; align-items: center; justify-content: center; }

  .back .brand { right: 34px; top: 30px; text-align: right; }
  .back .brand-tag { padding-left: 0; }

  .offer-list { position: absolute; left: 44px; top: 112px; }
  .offer-group { border-bottom: 1px solid rgba(255,255,255,.35); padding: 4px 0 6px; }
  .offer-group:last-child { border-bottom: none; }
  .offer-title { font-size: 14px; font-weight: 700; letter-spacing: .5px; text-transform: uppercase; }
  .offer-items { font-size: 13px; color: var(--ink-soft); }
</style>
</head>
<body>
<main class="sheet">

  <section class="card front" aria-label="Business card front">
    <svg class="card-art" viewBox="0 0 540 308" aria-hidden="false">
      <defs>
        <linearGradient id="blueInterior" x1="0" y1="0" x2="1" y2="1">
          <stop offset="0" stop-color="var(--photo-blue-a)"/>
          <stop offset="1" stop-color="var(--photo-blue-b)"/>
        </linearGradient>
        <linearGradient id="greenInterior" x1="0" y1="0" x2="1" y2="1">
          <stop offset="0" stop-color="var(--photo-green-a)"/>
          <stop offset="1" stop-color="var(--photo-green-b)"/>
        </linearGradient>
      </defs>
      <path d="M150,0 C260,96 430,124 540,52" fill="none" stroke="var(--rule)" stroke-width="10"/>
      <path role="img" aria-label="Photo of a limousine interior with blue and coloured party lights"
            d="M150,0 H540 V46 C430,116 260,92 150,0 Z" fill="url(#blueInterior)"/>
      <path d="M0,210 C110,150 230,176 300,308" fill="none" stroke="var(--rule)" stroke-width="10"/>
      <path role="img" aria-label="Photo of a party bus interior with green lighting and leather seats"
            d="M0,308 V218 C110,160 226,186 290,308 Z" fill="url(#greenInterior)"/>
    </svg>

    <div class="brand">
      <span class="brand-name">Marlow Limousine</span>
      <span class="brand-tag">&amp; Transportation</span>
    </div>

    <div class="contact">
      <p class="contact-name">Employee Name</p>
      <p class="contact-role">Managing Director</p>
      <p class="contact-line">
        <span class="contact-icon">
          <svg width="10" height="10" viewBox="0 0 10 10"><rect x="2" y="0.5" width="6" height="9" rx="1" fill="none" stroke="#000" stroke-width="1.2"/></svg>
        </span>123 456 7890
      </p>
      <p class="contact-line">
        <span class="contact-icon">
          <svg width="10" height="10" viewBox="0 0 10 10"><rect x="0.8" y="2" width="8.4" height="6" fill="none" stroke="#000" stroke-width="1.1"/><path d="M0.8,2 L5,5.6 L9.2,2" fill="none" stroke="#000" stroke-width="1.1"/></svg>
        </span>you@yourmail.example
      </p>
    </div>
  </section>

  <section class="card back" aria-label="Business card back">
    <svg class="card-art" viewBox="0 0 540 308">
      <defs>
        <linearGradient id="faintLimo" x1="0" y1="0" x2="1" y2="0">
          <stop offset="0" stop-color="var(--card)"/>
          <stop offset=".5" stop-color="var(--silhouette)"/>
          <stop offset="1" stop-color="var(--card)"/>
        </linearGradient>
      </defs>
      <rect role="img" aria-label="Faint photo of a stretch limousine in the background"
            x="20" y="100" width="500" height="160" rx="30" fill="url(#faintLimo)"/>
    </svg>

    <div class="brand">
      <span class="brand-name">Marlow Limousine</span>
      <span class="brand-tag">&amp; Transportation</span>
    </div>

    <div class="offer-list">
      <div class="offer-group">
        <p class="offer-title">Service</p>
        <p class="offer-items">weddings | birthdays | proms | airport transportation</p>
      </div>
      <div class="offer-group">
        <p class="offer-title">Service Areas</p>
        <p class="offer-items">houston | the woodlands | spring | tomball | cypress | kingwood</p>
      </div>
      <div class="offer-group">
        <p class="offer-title">Vehicle Types</p>
        <p class="offer-items">sedans | suvs | limos | party bus</p>
      </div>
    </div>
  </section>

</main>
</body>
</html>
```